ONE PAGE WEBSITE for Cool Recruitment Agency

Hello creative gurus,

We're are after a ONE PAGE World Press web design.

We're a recruitment start-up specializing in Information Technology.

The design should be cool, quirky and NOT mainstream.

The kind of web designs we like:

http://www.brivontek.co.za/#what-we-do
http://foldthelantern.com/
http://www.kelzo.com/index.html#home
http://marekvillandro.com/#/selected-works

And, we only like the front page of this web site: http://www.dunbywhim.com/

Any questions, please do let us know!

Thank you, and happy creating!

Dara
Updates

Reason: Just need a day or two to finalize everything. Thanks, Dara

Target Market(s)

Companies, employees, candidates

Industry/Entity Type

Recruitment

Coding

Coded - Design and coding required

Colors
f37122
f68e4e
ffcf3e
00a990
86cfc6
fcca95
fee18a

Requirements
Must have
• 1. The website should be techy, cool, funky, quirky and user-friendly.
• 2. Mobile-compatible
• 3. Please use our spaceman logo through the website (attached).
• 4. Please see attached website content/brief.
• 5. Colors - orange color is a must, but please use other colors to spice it up - make it more fun.
• The kind of web designs we like:
• http://www.brivontek.co.za/#what-we-do
• http://foldthelantern.com/
• http://www.kelzo.com/index.html#home
• http://marekvillandro.com/#/selected-works
• http://www.dunbywhim.com/
• Any questions, please do let us know!
Should not have
• -NO stock image banners, photos, images

```html
<!DOCTYPE html>
<html lang="en">
<head>
<meta charset="utf-8">
<title>Orbivo Talent</title>
<link rel="stylesheet" href="https://fonts.googleapis.com/css2?family=Nunito+Sans:wght@400;600;700;800&family=Open+Sans:wght@400;600&display=swap">
<style>
  :root {
    --orange: #ff6d00;
    --orange-soft: #f68e4e;
    --peach: #fcca95;
    --sun: #ffcf3e;
    --sun-soft: #fee18a;
    --teal: #00a990;
    --teal-soft: #86cfc6;
    --ink: #111111;
    --charcoal: #3a3a3a;
    --text: #444444;
    --nav-text: #555555;
    --rule: #cfcfcf;
    --button: #2f2f2f;
    --footer: #2b2b2b;
    --white: #ffffff;
  }
  * { box-sizing: border-box; margin: 0; padding: 0; }
  html, body { width: 1200px; height: 785px; overflow: hidden; background: var(--white); }
  body { position: relative; font-family: "Nunito Sans", sans-serif; color: var(--text); }

  .brand { position: absolute; left: 103px; top: 17px; width: 290px; height: 74px; }
  .brand-mark { position: absolute; left: 0; top: 0; width: 71px; height: 71px; border-radius: 50%; background: var(--ink); }
  .brand-name { position: absolute; left: 75px; top: 46px; font-size: 29px; line-height: 29px; font-weight: 800; color: var(--ink); letter-spacing: 6px; }

  .main-nav { position: absolute; left: 96px; top: 148px; width: 208px; list-style: none; }
  .main-nav li { height: 40px; border-bottom: 1px solid var(--rule); display: flex; align-items: center; padding-left: 23px; font-size: 16px; color: var(--nav-text); letter-spacing: 0.2px; white-space: nowrap; }
  .main-nav li:last-child { border-bottom: none; }
  .main-nav li.is-active { color: var(--orange); }

  .welcome { position: absolute; left: 364px; top: 156px; width: 370px; }
  .welcome-kicker { font-size: 24px; font-weight: 700; color: var(--ink); line-height: 28px; letter-spacing: -0.2px; }
  .welcome-title { font-size: 31px; font-weight: 700; color: var(--orange); line-height: 38px; margin-bottom: 20px; letter-spacing: -0.2px; }
  .welcome p { font-size: 14.3px; line-height: 21.3px; color: var(--text); margin-bottom: 22px; white-space: nowrap; }
  .read-more { position: absolute; left: 363px; top: 394px; width: 118px; height: 36px; border-radius: 3px; background: linear-gradient(#444, var(--button)); color: var(--white); font-size: 12px; font-weight: 700; display: flex; align-items: center; justify-content: center; letter-spacing: 0.2px; }

  .hiring-art { position: absolute; left: 735px; top: 166px; width: 372px; height: 250px;
    background: radial-gradient(circle at 70% 45%, rgba(255,109,0,0.55), rgba(255,109,0,0) 45%),
                radial-gradient(circle at 30% 60%, rgba(58,58,58,0.28), rgba(58,58,58,0) 50%),
                linear-gradient(135deg, #fff1e4, #ffd2ac 55%, #f2f2f2);
    border-radius: 4px; }

  .why-band { position: absolute; left: 103px; top: 467px; width: 994px; height: 233px; background: var(--orange); color: var(--white); font-family: "Open Sans", sans-serif; }
  .why-title { position: absolute; left: 42px; top: 34px; font-family: "Nunito Sans", sans-serif; font-size: 26px; line-height: 32px; font-weight: 400; letter-spacing: 0.6px; }
  .why-point { position: absolute; top: 81px; display: flex; gap: 8px; font-size: 13.2px; line-height: 21.3px; white-space: nowrap; }
  .why-point svg { flex: none; margin-top: 1px; }
  .why-point--expertise { left: 29px; }
  .why-point--service { left: 378px; }
  .why-point--empathy { left: 692px; }
  .why-call { position: absolute; left: 0; right: 0; top: 199px; text-align: center; font-size: 14.5px; font-weight: 600; }

  .site-footer { position: absolute; left: 0; top: 715px; width: 1200px; height: 70px; background: var(--footer); color: var(--white); }
  .copyright { position: absolute; left: 114px; top: 25px; font-size: 14px; }
  .social-links { position: absolute; left: 920px; top: 24px; display: flex; gap: 29px; list-style: none; }
  .social-links li { width: 19px; height: 19px; border-radius: 50%; }
  .social-links li:nth-child(1) { background: var(--teal-soft); }
  .social-links li:nth-child(2) { background: var(--sun); }
  .social-links li:nth-child(3) { background: var(--orange-soft); }
  .social-links li:nth-child(4) { background: var(--teal); }
</style>
</head>
<body>
  <header class="brand">
    <span class="brand-mark"></span>
    <span class="brand-name">ORBIVO</span>
  </header>

  <ul class="main-nav">
    <li class="is-active">HOME</li>
    <li>COMPANIES</li>
    <li>TALENT</li>
    <li>REFERALS</li>
    <li>ABOUT US</li>
    <li>BLOG</li>
    <li>CONTACT US</li>
  </ul>

  <section class="welcome">
    <h2 class="welcome-kicker">WELCOME TO</h2>
    <h1 class="welcome-title">ORBIVO TALENT</h1>
    <p>We’re Sydney’s IT talent specialists. We are<br>passionate, with boundless energy, and work to<br>bring great people together.</p>
    <p>We specialise in permanent and contract recruitment<br>solutions across Information Technology.</p>
  </section>
  <div class="read-more">READ MORE</div>

  <div class="hiring-art" role="img" aria-label="Illustration of a 'We are hiring' banner with recruiter figures, speech bubbles and a magnifying glass"></div>

  <section class="why-band">
    <h2 class="why-title">Why work with us?</h2>
    <div class="why-point why-point--expertise">
      <svg width="20" height="20" viewBox="0 0 20 20"><circle cx="10" cy="10" r="10" fill="#fff"/><path d="M5.5 10.2l3 3 6-6" fill="none" stroke="#ff6d00" stroke-width="2.4" stroke-linecap="round" stroke-linejoin="round"/></svg>
      <p>We’re experts in our field and have years of<br>hands-on experience in the I.T. industry. We know<br>our market intimately and understand the unique<br>skills required to build a successful I.T. team</p>
    </div>
    <div class="why-point why-point--service">
      <svg width="20" height="20" viewBox="0 0 20 20"><circle cx="10" cy="10" r="10" fill="#fff"/><path d="M5.5 10.2l3 3 6-6" fill="none" stroke="#ff6d00" stroke-width="2.4" stroke-linecap="round" stroke-linejoin="round"/></svg>
      <p>We offer a bespoke service with<br>dedicated account manager (a nice one!)<br>who will stay in regular contact with you</p>
    </div>
    <div class="why-point why-point--empathy">
      <svg width="20" height="20" viewBox="0 0 20 20"><circle cx="10" cy="10" r="10" fill="#fff"/><path d="M5.5 10.2l3 3 6-6" fill="none" stroke="#ff6d00" stroke-width="2.4" stroke-linecap="round" stroke-linejoin="round"/></svg>
      <p>We walk in your shoes. We’ve been on<br>the other side of the recruitment<br>process - your side (wether you’re a<br>talent or an employer),</p>
    </div>
    <p class="why-call">Call us on 0207 555 0142 or say “hello” at hello@orbivotalent.com</p>
  </section>

  <footer class="site-footer">
    <p class="copyright">© 2017 Company Name&nbsp; All right reserved&nbsp; Term of Use</p>
    <ul class="social-links" aria-label="Social links">
      <li></li><li></li><li></li><li></li>
    </ul>
  </footer>
</body>
</html>
```